Brook Vantage claims recovery services

Its a new company in Dubai UAE. The company activity is debt management, debt collection, loans settlements and restructuring. The company involved in any business or sector requires debt management including government entities, Medical & Health care sector, Banks & finance companies, SME's and commercial business.

Target Market(s)

government entities, Medical & Health care sector, Banks & finance companies, SME's and commercial business.

Industry/Entity Type

Financial Service

Number of Pages Required

5+ page

Requirements
Must have
• Focus on the services not the team and clients
Should not have
• Colorful . Shouldn't have Client testimonial and our clients

```html
<!DOCTYPE html>
<html lang="en">
<head>
<meta charset="utf-8">
<title>Brook Vantage — Claims Recovery Services</title>
<link href="https://fonts.googleapis.com/css2?family=Roboto:wght@400;500;700;900&family=Josefin+Sans:wght@300;400&family=Quicksand:wght@400;500&family=Open+Sans:wght@400;600&display=swap" rel="stylesheet">
<style>
:root{
  --navy:#1c2b48;
  --blue-dark:#24578a;
  --blue-mid:#2b7b96;
  --teal:#2b9181;
  --ink:#222;
  --muted:#555;
  --footer:#232323;
  --footer-text:#e6e6e6;
  --white:#fff;
}
*{margin:0;padding:0;box-sizing:border-box}
html,body{width:768px;height:1200px;overflow:hidden;background:var(--white)}
body{position:relative;font-family:"Open Sans",sans-serif;color:var(--ink)}
.abs{position:absolute}

.site-header{left:0;top:0;width:768px;height:86px;background:var(--white)}
.brand{left:60px;top:28px;display:flex;align-items:center;gap:8px;font-family:"Roboto",sans-serif;font-weight:500;font-size:18px;color:var(--navy);letter-spacing:.5px}
.brand-mark{width:20px;height:20px;background:var(--navy)}
.main-nav{left:470px;top:37px;display:flex;gap:18px;font-family:"Roboto",sans-serif;font-size:10.5px;color:#111}
.main-nav span{display:flex;align-items:center;gap:6px}

.hero{left:0;top:86px;width:768px;height:312px;background:linear-gradient(135deg,#8aa1b8 0%,#b8c6d4 40%,#9fb2c4 70%,#7e94ab 100%)}
.hero-shade{left:0;top:0;width:100%;height:100%;background:rgba(40,60,90,.35)}
.hero-title{left:0;top:118px;width:768px;text-align:center;font-family:"Roboto",sans-serif;font-weight:900;font-size:34px;color:var(--white);letter-spacing:-1.5px}
.hero-sub{left:0;top:156px;width:768px;text-align:center;font-family:"Roboto",sans-serif;font-weight:500;font-size:12.5px;color:var(--white);letter-spacing:-.4px}
.btn{display:flex;align-items:center;justify-content:center;font-family:"Roboto",sans-serif;font-weight:700;font-size:11px;color:var(--white);border-radius:4px}
.btn-tour{left:256px;top:190px;width:120px;height:35px;border:2px solid var(--white)}
.btn-diff{left:384px;top:190px;width:135px;height:35px;background:var(--blue-dark);font-size:10px}

.service{top:398px;height:194px;color:var(--white);text-align:center}
.service h2{font-family:"Roboto",sans-serif;font-weight:500;font-size:17px;margin-top:44px;letter-spacing:.3px}
.service p{font-size:7.8px;line-height:1.3;margin:20px 6px 0}
.service .more{position:absolute;left:50%;transform:translateX(-50%);bottom:20px;width:81px;height:25px;border-radius:13px;background:var(--white);color:#333;font-family:"Quicksand",sans-serif;font-size:10px;display:flex;align-items:center;justify-content:center}
.svc-recovery{left:0;width:256px;background:var(--blue-dark)}
.svc-management{left:256px;width:267px;background:linear-gradient(90deg,#27698f,#2c8296)}
.svc-counselling{left:523px;width:245px;background:var(--teal)}

.profile-photo{left:38px;top:612px;width:262px;height:188px;background:radial-gradient(ellipse at 55% 45%,#9bb6cf 0%,#c8d8e6 45%,#fff 80%)}
.profile-name{left:351px;top:616px;font-family:"Roboto",sans-serif;font-weight:700;font-size:23px;color:var(--navy);letter-spacing:-.8px}
.profile-rule{left:352px;top:657px;width:67px;height:3px;background:#ddd}
.profile-role{left:348px;top:676px;font-family:"Josefin Sans",sans-serif;font-weight:300;font-size:21px;line-height:26px;color:var(--navy);letter-spacing:.5px}
.profile-text{left:348px;top:735px;width:396px;font-family:"Roboto",sans-serif;font-size:10px;line-height:12px;color:#222}

.stat{top:885px;width:130px;text-align:center;color:var(--navy)}
.stat svg{display:block;margin:0 auto;height:28px}
.stat .num{font-family:"Quicksand",sans-serif;font-weight:500;font-size:28px;line-height:32px;margin-top:4px}
.stat .label{font-family:"Open Sans",sans-serif;font-size:9px;color:var(--muted)}

.site-footer{left:0;top:1025px;width:768px;height:175px;background:var(--footer);color:var(--footer-text);font-family:"Open Sans",sans-serif}
.foot-links{left:39px;top:22px;font-size:9.5px;line-height:12.8px}
.foot-heading{font-weight:600;font-size:11.5px}
.foot-contact{left:208px;top:20px}
.contact-row{display:flex;align-items:center;gap:6px;font-size:9.5px;margin-top:15px}
.contact-row:first-of-type{margin-top:14px}
.foot-history{left:398px;top:21px;width:190px}
.foot-history p{font-size:9.5px;line-height:12.8px;margin-top:16px}
.foot-map{left:634px;top:17px;width:100px;height:84px;background:linear-gradient(135deg,#8a8a8a,#a9a9a9)}
.foot-note{left:624px;top:111px;width:136px;font-size:9.5px;line-height:12.8px;text-align:center}
</style>
</head>
<body>

<header class="site-header abs">
  <div class="brand abs"><span class="brand-mark"></span>Brook Vantage</div>
  <nav class="main-nav abs">
    <span>Home</span>
    <span>Services <svg width="7" height="5" viewBox="0 0 7 5"><path d="M0 0h7L3.5 5z" fill="#111"/></svg></span>
    <span>About Us</span>
    <span>Contact Us</span>
  </nav>
</header>

<section class="hero abs" role="img" aria-label="Overhead photo of a desk with a laptop, clipboard, glasses and stethoscope">
  <div class="hero-shade abs"></div>
  <h1 class="hero-title abs">MAKING DEPT WORK FOR YOU!</h1>
  <p class="hero-sub abs">Our success is built on traditions of trust, valued relationships, andrespect.</p>
  <a class="btn btn-tour abs">TAKE A TOUR</a>
  <a class="btn btn-diff abs">THE BROOK DIFFERENCE</a>
</section>

<section class="service svc-recovery abs">
  <h2>Recovery Solutions</h2>
  <p>Our experience has taught us that when it comes to recovery, it always pays to find the most amicable solution, and we work hard to make this happen The Brook Vantage team is trained in communication.</p>
  <a class="more">Learn More</a>
</section>
<section class="service svc-management abs">
  <h2>Debt Management</h2>
  <p>At Brook Vantage, we pull together our wisdom and expertise to make debt work for you.Our debt management services bring together thorough analysis careful planning and realistic budgeting to help you manage your debt.</p>
  <a class="more">Learn More</a>
</section>
<section class="service svc-counselling abs">
  <h2>Debt Counselling</h2>
  <p>Take charge of your debt with guidance from our experts. Education, planning and budgeting will help you to not only manage current debt, but also plan for the future.</p>
  <a class="more">Learn More</a>
</section>

<div class="profile-photo abs" role="img" aria-label="Photo of a smiling man with arms spread wide"></div>
<h2 class="profile-name abs">DANIEL REYES</h2>
<div class="profile-rule abs"></div>
<p class="profile-role abs">BUSINESSMAN,<br>HAPPY FATHER</p>
<p class="profile-text abs">Our work spans a diverse range of sectors including medical and health care, government agencies, media, real estate, commercial companies and SMEs.We're proud of our work, and of our great relationship with our clients. No case is too big, or too small.</p>

<div class="stat abs" style="left:90px">
  <svg viewBox="0 0 32 24" width="32"><path d="M2 12Q16 -2 30 12Q16 26 2 12Z" fill="none" stroke="#1c2b48" stroke-width="3"/><circle cx="16" cy="12" r="4" fill="#1c2b48"/></svg>
  <div class="num">8774</div><div class="label">VIST RECEIVE</div>
</div>
<div class="stat abs" style="left:244px">
  <svg viewBox="0 0 28 28" width="28"><path d="M3 3h22v4H3zM2 9h24v4H2zM5 13h18v13H5z" fill="none" stroke="#1c2b48" stroke-width="2.4"/><rect x="11" y="17" width="6" height="9" fill="#1c2b48"/></svg>
  <div class="num">10000</div><div class="label">BRANCHES</div>
</div>
<div class="stat abs" style="left:401px">
  <svg viewBox="0 0 28 28" width="28"><path d="M14 3C7 3 3 7.5 3 12.5c0 3 1.5 5.5 4 7.2L6 25l5.5-3.2c.8.2 1.6.2 2.5.2 7 0 11-4.5 11-9.5S21 3 14 3z" fill="none" stroke="#1c2b48" stroke-width="2"/></svg>
  <div class="num">4475</div><div class="label">FOLLOWERS</div>
</div>
<div class="stat abs" style="left:558px">
  <svg viewBox="0 0 30 24" width="30"><g fill="#1c2b48"><circle cx="5" cy="6" r="2.5"/><circle cx="15" cy="4" r="3"/><circle cx="25" cy="6" r="2.5"/><rect x="2" y="10" width="6" height="10" rx="2"/><rect x="11" y="9" width="8" height="13" rx="2"/><rect x="22" y="10" width="6" height="10" rx="2"/></g></svg>
  <div class="num">1000</div><div class="label">EMPLOYEES</div>
</div>

<footer class="site-footer abs">
  <div class="foot-links abs">Home<br>Services<br>Contact Us<br>About Us<br>Policy<br>Term and Conditions<br>Privacy<br>Cookies</div>
  <div class="foot-contact abs">
    <div class="foot-heading">Contact Info :</div>
    <div class="contact-row"><svg width="9" height="13" viewBox="0 0 9 13"><path d="M4.5 0A4.5 4.5 0 0 0 0 4.5C0 8 4.5 13 4.5 13S9 8 9 4.5A4.5 4.5 0 0 0 4.5 0z" fill="#e0463a"/><circle cx="4.5" cy="4.5" r="1.6" fill="#232323"/></svg>Unit 402, Marina Plaza, Dubai, UAE</div>
    <div class="contact-row"><svg width="11" height="11" viewBox="0 0 11 11"><rect width="11" height="11" rx="2" fill="#2e9b78"/><path d="M3 2.5l1.5 1.6-.7 1c.5 1 1.2 1.7 2.2 2.2l1-.7L8.5 8 7.6 9C5 8.6 2.4 6 2 3.4z" fill="#fff"/></svg>+971-4-555-01827</div>
    <div class="contact-row"><svg width="13" height="11" viewBox="0 0 13 11"><path d="M0 4.5L6.5 0 13 4.5V11H0z" fill="#3fae6c"/><path d="M0 4.5l6.5 4 6.5-4" fill="none" stroke="#fff" stroke-width="1"/></svg>info@brookvantage.ae</div>
  </div>
  <div class="foot-history abs">
    <div class="foot-heading">Company History</div>
    <p>Lorem ipsum dolor sit amet,<br>feugiat delicata liberavisse id cum,<br>no quo maiorum intellegebat, liber<br>regione eu sit. Mea cu case ludus integre,<br>vide viderer eleifend ex mea</p>
  </div>
  <div class="foot-map abs" role="img" aria-label="Street map showing the office location"></div>
  <p class="foot-note abs">Lorem ipsum dolor sit am et, feugiat delicata liberavisse id cum, no quo maiorum intell egebat, liber</p>
</footer>

</body>
</html>
```